HM Marketing Piece

Heron Meadow was created in 1984 as a shared aircraft ownership comprised of individual stockholders, interested in sharing the cost of aircraft ownership. Our strategy is simple, make owning and flying well maintained and upgraded aircraft more affordable through shared ownership.

When you own an aircraft individually, you have all the costs of a loan, hangar, insurance, subscriptions, annual inspection, and those unscheduled maintenance issues.

When you rent an aircraft from a local FBO, you get well used, dirty aircraft that everyone abuses with minimum hour requirements for weekend getaways that turn a 2 hour trip into a 9 hour hit on your wallet.

The solution? Shared aircraft ownership. Heron Meadow has three aircraft based out of Bramwell Field (KQLP). When you join a partnership, you split fixed costs between multiple individuals, AND get access to multiple well maintained and upgraded aircraft. When you fly, you pay the variable costs of your flight time only. Dividing the fixed expenses among multiple members makes flying much more affordable.

Benefits of shared aircraft ownership:

• Much cheaper than owning an aircraft individually
• Access to multiple aircraft
• Higher quality aircraft than your local FBO

• Hangared aircraft, flown by owners, not renters
• No overnight minimums
• On-line scheduling

www.heronmeadowfly.example

```html
<!DOCTYPE html>
<html lang="en">
<head>
<meta charset="utf-8">
<title>Heron Meadow – Marketing Postcard</title>
<link href="https://fonts.googleapis.com/css2?family=Cinzel:wght@400;600&family=Crimson+Text:wght@600&display=swap" rel="stylesheet">
<style>
  :root{
    --page:#e9e6e1;
    --navy:#1d3557;
    --ink:#111a24;
    --red:#b3202a;
    --sky-deep:#5f8fcf;
    --sky-mid:#a9c6ea;
    --sky-light:#eef4fb;
    --tarmac:#4b4a45;
    --line:#6b6f75;
    --white:#ffffff;
  }
  *{box-sizing:border-box;margin:0;padding:0}
  html,body{width:848px;height:1200px;overflow:hidden;background:var(--page)}
  .card{position:absolute;left:84px;width:680px;height:500px;overflow:hidden;
        box-shadow:0 4px 14px rgba(0,0,0,.25);background:var(--white)}
  .card--front{top:50px}
  .card--back{top:630px;
    background:linear-gradient(160deg,var(--sky-mid) 0%,var(--sky-light) 35%,#d6e4f4 60%,var(--sky-light) 85%,#c3d7ef 100%)}

  /* front */
  .front-photo{position:absolute;inset:0;
    background:linear-gradient(180deg,#4f82c6 0%,#9fbfe3 33%,#5b7a4c 40%,#e8ecef 48%,#c9ccd0 58%,var(--tarmac) 70%,#3c3b37 100%)}
  .front-panel{position:absolute;inset:0;width:680px;height:500px}
  .brand{position:absolute;right:26px;top:36px;font-family:"Cinzel",serif;
    font-size:29px;font-weight:400;color:var(--navy);letter-spacing:1px}
  .benefits-title{position:absolute;right:24px;top:140px;width:260px;text-align:right;
    font-family:"Cinzel",serif;font-size:17px;line-height:1.15;color:var(--red)}
  .benefits{position:absolute;left:352px;top:212px;width:310px;list-style:none;
    font-family:"Cinzel",serif;font-size:13px;line-height:1.2;color:var(--ink)}
  .benefits li::before{content:"\203A\00a0"}
  .benefits li.gap{margin-top:10px}
  .phone{position:absolute;right:22px;bottom:24px;display:flex;align-items:center;gap:6px;
    font-family:"Crimson Text",serif;font-size:17px;color:var(--ink)}
  .site{position:absolute;left:34px;bottom:18px;font-family:"Cinzel",serif;
    font-size:14px;color:var(--white);letter-spacing:.5px}

  /* back */
  .about{position:absolute;left:24px;top:38px;width:440px;text-align:center;
    font-family:"Crimson Text",serif;font-size:14.5px;line-height:1.3;color:var(--ink)}
  .stamp{position:absolute;right:30px;top:22px;width:150px;height:142px;
    border:2px dashed #2a2a2a}
  .photo{position:absolute;left:24px;width:256px}
  .photo--upper{top:176px;height:164px;
    background:linear-gradient(180deg,#3f6fae 0%,#8fb0d8 40%,#4f6a42 46%,#c9ccd0 55%,#55544f 100%)}
  .photo--lower{top:340px;height:176px;
    background:linear-gradient(180deg,#5e8fd0 0%,#a8c4e6 40%,#6a7c5a 46%,#b7babd 58%,#4c4b47 100%)}
  .address{position:absolute;left:322px;top:228px;width:310px;height:110px}
</style>
</head>
<body>

<section class="card card--front">
  <div class="front-photo" role="img" aria-label="Photo of a white single-engine high-wing aircraft parked on a tarmac under a blue sky"></div>
  <svg class="front-panel" viewBox="0 0 680 500" aria-hidden="true">
    <defs>
      <linearGradient id="panelSky" x1="0" y1="0" x2="0.4" y2="1">
        <stop offset="0" stop-color="#7ea6dc"/>
        <stop offset="0.3" stop-color="#eef4fb"/>
        <stop offset="0.55" stop-color="#c8daf0"/>
        <stop offset="0.8" stop-color="#f2f6fb"/>
        <stop offset="1" stop-color="#8fb3e2"/>
      </linearGradient>
    </defs>
    <path d="M372 0 C300 150 300 380 418 500 L680 500 L680 0 Z" fill="url(#panelSky)" stroke="rgba(0,0,0,.25)" stroke-width="3"/>
  </svg>
  <h1 class="brand">Heron Meadow</h1>
  <h2 class="benefits-title">Benefits of shared aircraft ownership:</h2>
  <ul class="benefits">
    <li>Much cheaper than owning an aircraft individually</li>
    <li>Access to multiple aircraft</li>
    <li>Higher quality aircraft than your local FBO</li>
    <li class="gap">Hangared aircraft, flown by owners, not renters</li>
    <li>No overnight minimums</li>
    <li>On-line scheduling</li>
  </ul>
  <div class="phone">
    <svg width="22" height="18" viewBox="0 0 22 18" aria-hidden="true">
      <path d="M1 6 C1 1 21 1 21 6 L21 8 L16 8 L15 5 L7 5 L6 8 L1 8 Z" fill="#111a24"/>
      <path d="M6 9 L16 9 L19 17 L3 17 Z" fill="#111a24"/>
      <circle cx="11" cy="13" r="2" fill="#fff"/>
    </svg>
    <span>555-014-2290</span>
  </div>
  <div class="site">www.heronmeadowfly.example</div>
</section>

<section class="card card--back">
  <p class="about">Heron Meadow was created in 1984 as a shared aircraft ownership comprised of individual stockholders, interested in sharing the cost of aircraft ownership. Our strategy is simple, make owning and flying well maintained and upgraded aircraft more affordable through shared ownership.</p>
  <div class="stamp"></div>
  <div class="photo photo--upper" role="img" aria-label="Photo of a low-wing single-engine aircraft with blue trim parked on the ramp"></div>
  <div class="photo photo--lower" role="img" aria-label="Photo of a silver low-wing single-engine aircraft on the apron"></div>
  <svg class="address" viewBox="0 0 310 110" aria-hidden="true">
    <g stroke="#6b6f75" stroke-width="1.2" stroke-dasharray="6 3">
      <line x1="0" y1="2" x2="310" y2="2"/>
      <line x1="0" y1="36" x2="310" y2="36"/>
      <line x1="0" y1="70" x2="310" y2="70"/>
      <line x1="0" y1="104" x2="310" y2="104"/>
    </g>
  </svg>
</section>

</body>
</html>
```